New Orleans history and Handbook for Accredited Sightseeing Host - City of New Orleans

Book cover. Paperback, 5.25” x 8” book cover, 172 pages, White paper, PrintHarbor template – attached. (PrintHarbor names the template as 180 pages)

This book puts the history of New Orleans into easy sections for persons to learn who are preparing to take the test for the Municipal Certified Visitor Escort Permit. It is required of all tour guides in the city. The attached text for the back cover gives a more complete synopsis of the content.

This Study Guide is a resource for persons seeking a tour guide license. We would like the cover to reflect the professionalism required for test preparation and carry a subtle connection to the creativity of the author as a storyteller and entertainer in the city of New Orleans.

An idea we have had for the front cover would have a background of stylized map of the famed Brindle Ward in the lower half of the cover. Possibly a fan shaped perspective view. The central focus of the Brindle Ward, and the city, is St. Anselm Basilica and Halvorsen Plaza as seen in these maps and images. https://lnkshrt.example/q7Xr2M Maps old and new - https://lnkshrt.example/v9TpWd. A map is not a requirement for cover. Creativity is.

Attached is PrintHarbor/Zentrova template, text for front and back cover and two photographs of the author for you to choose from. Both need photoshopping to remove persons behind or next Mr Pembry.

Authors’ previous book: 'Over By The River: Quiet Tales of a Harbor Town' by Harold Pembry Link: http://bkl.example/7T2QWZP

Target Market(s)

Persons 18+

Industry/Entity Type

Tourism

Font styles to use
Serif

Requirements
Must have
• Design with book front and back cover with: spine.
• Primary Title is : Handbook for Accredited Sightseeing Host Permit Exam
• Sub-title: City of New Orleans
Nice to have
• Possible image for design is a Fleur-de-lis, an official emblem of New Orleans. This is a design option and not .a serious Nice To Have.. Some inspiration https://lnkshrt.example/k3FzYb

```html
<!DOCTYPE html>
<html lang="en">
<head>
<meta charset="utf-8">
<title>Handbook for the Accredited Sightseeing Host Exam – Cover</title>
<link rel="stylesheet" href="https://fonts.googleapis.com/css2?family=Cinzel:wght@400;500&family=Montserrat:wght@600&family=Source+Sans+3:ital,wght@0,400;0,700;0,800;1,700&display=swap">
<style>
  :root {
    --ink: #1b1b1b;
    --maroon: #8c2b2b;
    --navy: #123150;
    --navy-deep: #0b2440;
    --back-top: #ffffff;
    --back-bottom: #a9cde4;
    --spine-top: #eaf3f9;
    --spine-bottom: #a6cbe3;
    --frame: #f2c3a6;
    --sky-top: #dfeaf4;
    --sky-mid: #f3f6f9;
    --city-warm: #a99a86;
    --city-green: #5d7a4e;
  }
  * { margin: 0; padding: 0; box-sizing: border-box; }
  html, body { width: 1200px; height: 887px; overflow: hidden; background: #fff; }
  .cover { position: relative; width: 1200px; height: 887px; font-family: "Source Sans 3", sans-serif; color: var(--ink); }

  .back { position: absolute; left: 0; top: 0; width: 565px; height: 887px;
    background: linear-gradient(to bottom, var(--back-top) 0%, #dcebf4 45%, var(--back-bottom) 100%); }
  .spine { position: absolute; left: 565px; top: 0; width: 70px; height: 887px;
    background: linear-gradient(to bottom, var(--spine-top), var(--spine-bottom)); }
  .front { position: absolute; left: 635px; top: 0; width: 565px; height: 887px; overflow: hidden; }

  .kicker { font-family: "Montserrat", sans-serif; font-weight: 600; letter-spacing: 0.42em; text-align: center; }
  .title { font-weight: 800; text-align: center; line-height: 1.12; letter-spacing: -0.005em; }
  .place { font-family: "Cinzel", serif; text-align: center; }

  .back .kicker { position: absolute; left: 0; width: 565px; top: 34px; font-size: 26px; padding-left: 14px; }
  .back .title { position: absolute; left: 0; width: 565px; top: 74px; font-size: 46px; color: var(--maroon); }
  .back .place { position: absolute; left: 0; width: 565px; top: 186px; font-size: 26px; }
  .back .place small { font-size: 19px; }

  .author-photo { position: absolute; left: 40px; top: 244px; width: 268px; height: 216px;
    border: 2px solid var(--frame);
    background: linear-gradient(135deg, #6b6a3f 0%, #8e7f52 40%, #cfcab9 70%, #7b7a88 100%); }

  .blurb { position: absolute; font-size: 13.6px; line-height: 18.6px; text-align: justify; }
  .blurb p { text-indent: 0.5em; margin-bottom: 6px; }
  .blurb-left { left: 37px; top: 478px; width: 273px; }
  .blurb-right { left: 331px; top: 241px; width: 213px; }

  .companion { position: absolute; left: 39px; top: 796px; width: 290px; font-size: 16px; line-height: 20px; color: var(--maroon); }
  .companion em { font-weight: 700; }

  .spine-title { position: absolute; left: 0; top: 36px; width: 70px; height: 420px;
    writing-mode: vertical-rl; display: flex; flex-direction: column; align-items: center; }
  .spine-title .kicker { font-size: 19px; letter-spacing: 0.55em; color: var(--ink); line-height: 24px; text-align: left; }
  .spine-title .line { font-weight: 700; font-size: 19px; line-height: 22px; color: var(--ink); }
  .spine-author { position: absolute; left: 0; top: 448px; width: 70px; height: 420px;
    writing-mode: vertical-rl; display: flex; align-items: center;
    font-family: "Cinzel", serif; font-size: 25px; color: var(--navy); }

  .front-photo { position: absolute; inset: 0;
    background:
      radial-gradient(ellipse 70% 30% at 55% 100%, var(--city-green) 0%, transparent 70%),
      linear-gradient(to bottom, var(--sky-top) 0%, var(--sky-mid) 35%, #e6eef4 60%, #c9cdc9 68%, var(--city-warm) 80%, #8b8370 92%, var(--city-green) 100%); }
  .front-author { position: absolute; left: 0; width: 565px; top: 28px; font-family: "Cinzel", serif; font-size: 32px; text-align: center; color: var(--ink); }
  .front .kicker { position: absolute; left: 0; width: 565px; top: 146px; font-size: 30px; padding-left: 14px; color: var(--ink); }
  .front .title { position: absolute; left: 0; width: 565px; top: 190px; font-size: 58px; line-height: 66px;
    background: linear-gradient(to bottom, var(--navy) 0%, var(--navy-deep) 100%);
    -webkit-background-clip: text; background-clip: text; color: transparent; }
  .front .place { position: absolute; left: 0; width: 565px; top: 372px; font-size: 33px; line-height: 40px; color: var(--ink); }
  .front .place .big { display: block; font-size: 48px; line-height: 52px; }
</style>
</head>
<body>
<div class="cover">

  <section class="back">
    <div class="kicker">HANDBOOK FOR</div>
    <h2 class="title">ACCREDITED SIGHTSEEING<br>HOST PERMIT EXAM</h2>
    <div class="place"><small>CITY OF</small> NEW ORLEANS</div>

    <div class="author-photo" role="img" aria-label="Portrait of the author in a straw hat and glasses"></div>

    <div class="blurb blurb-left">
      <p>This <strong>STUDY GUIDE</strong> is designed to prepare a person for the Municipal Certified Visitor Escort Permit test. Laid out in simple, easy to learn sections this is the basic information needed for passing the city test and moving on to becoming an entertaining tour guide. Your knowledge of the history of New Orleans and Louisiana is key to earning money as a professional tour guide. Tips are directly related to the quality of your stories.</p>
      <p>This guide names the important people, places and events of the city. Recommended readings are based on the author’s own personal preferences for reference or pleasure reading.</p>
    </div>

    <div class="blurb blurb-right">
      <p>A special feature included is a seasoned written Brindle Ward Walking Tour complete with route, stops and full stories. The tour begins at the river and proceeds through a section of the Ward favored among tour guides. It is the bread and butter of Brindle Ward tours.</p>
      <p>Hal Pembry worked as a tour guide in the City for years. He taught the Professional Tourguiding class at Marlowe Community College, plus a class in Research and Storytelling. He is an avid reader of local history. He earned a Ph.D. from Westbrook University in Communication, plus BA and MA degrees from Bayou State University in Public Speaking.</p>
    </div>

    <p class="companion">A companion to this STUDY GUIDE is Dr. Pembry’s <em>OVER BY THE RIVER - Quiet Tales of a Harbor Town.</em></p>
  </section>

  <section class="spine">
    <div class="spine-title">
      <span class="kicker">HANDBOOK FOR</span>
      <span class="line">ACCREDITED SIGHTSEEING HOST EXAM</span>
    </div>
    <div class="spine-author">HAROLD C PEMBRY JR., PH.D.</div>
  </section>

  <section class="front">
    <div class="front-photo" role="img" aria-label="Aerial view of a cloudy sky over the old city, with the basilica and plaza below"></div>
    <div class="front-author">HAROLD C PEMBRY JR., PH.D.</div>
    <div class="kicker">HANDBOOK FOR</div>
    <h1 class="title">ACCREDITED<br>SIGHTSEEING HOST</h1>
    <div class="place">CITY OF<span class="big">NEW ORLEANS</span></div>
  </section>

</div>
</body>
</html>
```